New website for tarnholm.se using wordpress

- Tarnholm is a consultant broker based in Sweden
- Current web page: tarnholm.se
- We want a new web page and we are aiming for simple and "clean"
- Two target groups:
1. Consultants/Consultant firms looking for assignments
2. Clients looking for consultants
- Colors + Logo attached

Requirements
Must have
• The new site should have separate pages the different sections. We have to be able to link to each page separately. NOT like the current web page where all the content is on one page.

```html
<!DOCTYPE html>
<html lang="en">
<head>
<meta charset="utf-8">
<title>Tarnholm – Consultant brokerage</title>
<link href="https://fonts.googleapis.com/css2?family=Roboto:wght@400;500;700&display=swap" rel="stylesheet">
<style>
:root{
  --purple:#6a2fa0;
  --purple-deep:#5b2890;
  --ink:#3d3d3d;
  --text:#555555;
  --white:#ffffff;
  --black:#1b1b1b;
  --footer:#1f1f1f;
  --line:#3a3a3a;
}
*{margin:0;padding:0;box-sizing:border-box}
html,body{width:1200px;height:3124px;overflow:hidden}
body{font-family:'Roboto',Arial,sans-serif;color:var(--text);background:var(--white);position:relative}
.abs{position:absolute}

/* hero */
.hero{left:0;top:0;width:1200px;height:846px;
  background:radial-gradient(ellipse at 55% 30%,#b59a82 0%,#7f6e5c 30%,#4d4a3c 60%,#2b2e28 100%)}
.hero::after{content:"";position:absolute;inset:0;background:linear-gradient(90deg,rgba(20,20,20,.45),rgba(20,20,20,.15) 60%,rgba(20,20,20,.35))}
.brand-tab{left:112px;top:0;width:196px;height:182px;background:var(--purple);border-radius:0 0 34px 34px;z-index:2;
  display:flex;align-items:flex-end;justify-content:center;padding-bottom:34px}
.brand-tab span{color:var(--white);font-weight:700;font-size:36px;letter-spacing:.5px}
.main-nav{right:110px;top:48px;display:flex;gap:41px;z-index:2}
.main-nav a{color:var(--white);font-weight:700;font-size:16px;text-decoration:none;letter-spacing:.2px}
.hero-title{left:112px;top:362px;color:var(--white);font-weight:700;font-size:58px;line-height:70px;z-index:2}
.hero-btn{top:535px;width:170px;height:57px;border:3px solid var(--white);border-radius:30px;color:var(--white);
  font-weight:500;font-size:20px;display:flex;align-items:center;justify-content:center;z-index:2}
.dots{left:576px;top:816px;display:flex;gap:6px;z-index:2}
.dots i{width:13px;height:13px;border-radius:50%;background:var(--white)}
.dots i.on{background:#a06fd6}

/* about */
.about-photo{left:130px;top:922px;width:410px;height:490px;border-radius:38px;
  background:linear-gradient(135deg,#4a5a3c 0%,#8d8a78 35%,#e6e2dc 60%,#c9c4bc 100%)}
.section-title{font-weight:500;font-size:39px;color:var(--ink)}
.underline{height:3px;width:48px;background:var(--purple)}
.about-title{left:590px;top:934px}
.about-line{left:590px;top:984px}
.about-text{left:590px;top:1003px;width:480px;font-size:13.5px;line-height:25.7px;text-align:justify;font-family:Arial,sans-serif}
.about-text p+p{margin-top:25.7px}
.read-more{left:586px;top:1335px;width:176px;height:62px;background:var(--purple);border-radius:31px;color:var(--white);
  font-weight:700;font-size:17px;display:flex;align-items:center;justify-content:center}

/* assignments */
.assign-band{left:0;top:1494px;width:1200px;height:542px;background:linear-gradient(180deg,#6b31a2,#5e2a94)}
.assign-title{left:0;top:1546px;width:1200px;text-align:center;color:var(--white);font-weight:500;font-size:39px}
.assign-line{left:576px;top:1600px;background:var(--white)}
.tab{left:112px;width:319px;height:57px;background:#f8f8f8;border-radius:0 29px 29px 0;color:var(--ink);
  font-weight:500;font-size:17.5px;display:flex;align-items:center;padding-left:23px}
.tab.active{background:var(--black);color:var(--white)}
.detail-title{left:502px;top:1664px;color:var(--white);font-weight:500;font-size:26px}
.detail-line{left:502px;top:1710px;background:var(--white)}
.detail-text{left:502px;top:1741px;width:566px;color:var(--white);font-size:15px;line-height:25.7px;text-align:justify}

/* why */
.why-title{left:0;top:2080px;width:1200px;text-align:center}
.why-line{left:576px;top:2135px}
.why-frame{left:383px;top:2229px;width:705px;height:417px;border:1.5px solid var(--purple);border-left:none;border-top:none;
  border-radius:0 40px 40px 40px}
.why-frame::before{content:"";position:absolute;left:205px;top:0;right:-1.5px;height:40px;border-top:1.5px solid var(--purple);border-right:1.5px solid var(--purple);border-radius:0 40px 0 0}
.why-frame::after{content:"";position:absolute;left:-1.5px;bottom:-1.5px;width:40px;height:80px;border-left:1.5px solid var(--purple);border-bottom:1.5px solid var(--purple);border-radius:0 0 0 40px}
.why-photo{left:112px;top:2178px;width:476px;height:439px;border-radius:38px;
  background:linear-gradient(120deg,#e9ddd2 0%,#b9a593 35%,#56604c 60%,#d3d0cb 100%)}
.why-list{left:612px;top:2300px;list-style:none}
.why-list li{display:flex;align-items:center;gap:11px;height:60.5px;font-size:23px;color:var(--ink)}

/* footer */
.footer{left:0;top:2737px;width:1200px;height:387px;background:var(--footer)}
.foot-brand{left:0;top:2775px;width:1200px;text-align:center;color:var(--white);font-weight:700;font-size:66px;letter-spacing:1px}
.foot-nav{left:0;top:2890px;width:1200px;display:flex;justify-content:center;gap:57px}
.foot-nav a{color:var(--white);font-weight:700;font-size:16px;text-decoration:none}
.rule{left:112px;width:976px;height:1px;background:var(--line)}
.contact{top:2965px;display:flex;align-items:center;gap:17px;color:var(--white);font-family:Arial,sans-serif;font-size:15px;line-height:24px}
.ring{width:44px;height:44px;border:1.5px solid #bbbbbb;border-radius:50%;display:flex;align-items:center;justify-content:center;flex:none}
.social{left:112px;top:3062px;display:flex;gap:8px}
.social .ring{width:42px;height:42px;border:2px solid var(--white)}
.copy{right:112px;top:3074px;color:var(--white);font-family:Arial,sans-serif;font-size:15px}
</style>
</head>
<body>

<section class="abs hero" role="img" aria-label="Photo of a smiling consultant in conversation with a client at a desk"></section>
<div class="abs brand-tab"><span>Tarnholm</span></div>
<nav class="abs main-nav">
  <a href="#">CONSULTANT</a><a href="#">CLIENT</a><a href="#">ASSIGNMENT</a><a href="#">ABOUT US</a><a href="#">CONTACT US</a>
</nav>
<h1 class="abs hero-title">We facilitate<br>purchase of skills</h1>
<div class="abs hero-btn" style="left:112px">Consultant</div>
<div class="abs hero-btn" style="left:296px">Clients</div>
<div class="abs dots"><i></i><i class="on"></i><i></i></div>

<div class="abs about-photo" role="img" aria-label="Photo of a smiling businesswoman in a white blazer talking across a desk"></div>
<h2 class="abs section-title about-title">About Tarnholm</h2>
<div class="abs underline about-line"></div>
<div class="abs about-text">
  <p>Tarnholm is part of Velmora, whose focus is on staffing and recruitment, while we at Tarnholm focus on consulting brokerage services. We work professionally and personally and have broad experience in Finance, HR and IT. Our drive is to strengthen and supplement our customers' organizations with specialist knowledge in precisely these areas, including system development, project management, accounting, financial management and business development. With the help of our well-established network of subcontractors/partners, we can tailor the process as needed and simplify the purchasing of qualified skills.</p>
  <p>The name Tarnholm comes from Latin and translates to "problem solver, problem-free". Our ambition is to do just that for our customers; facilitate, solve problems and reduce friction in day-to-day operations.</p>
</div>
<div class="abs read-more">READ MORE</div>

<section class="abs assign-band"></section>
<h2 class="abs assign-title">Most Recent Assignments</h2>
<div class="abs underline assign-line"></div>
<div class="abs tab" style="top:1654px">Sed ut perspiciatis unde omnis</div>
<div class="abs tab active" style="top:1721px">Nemo enim ipsam volupta</div>
<div class="abs tab" style="top:1788px">Voluptatem sequi nesciunt</div>
<div class="abs tab" style="top:1855px">Error sit voluptatem accusantium</div>
<div class="abs tab" style="top:1922px">Nemo enim ipsam voluptatem</div>
<h3 class="abs detail-title">Nemo enim ipsam volupta</h3>
<div class="abs underline detail-line"></div>
<p class="abs detail-text">Sed ut perspiciatis unde omnis iste natus error sit voluptatem accusantium doloremque laudantium, totam rem aperiam, eaque ipsa quae ab illo inventore veritatis et quasi architecto beatae vitae dicta sunt explicabo. Nemo enim ipsam voluptatem quia voluptas sit aspernatur aut odit aut fugit, sed quia consequuntur magni dolores eos qui ratione voluptatem sequi nesciunt. Neque porro quisquam est, qui dolorem ipsum quia dolor sit amet, consectetur, adipisci velit, sed quia non numquam eius modi tempora incidunt ut labore et dolore magnam aliquam quaerat sit aspernatur quia consequuntur magni dolores eos qui ratione voluptatem.</p>

<h2 class="abs section-title why-title">Why Tarnholm</h2>
<div class="abs underline why-line"></div>
<div class="abs why-frame"></div>
<div class="abs why-photo" role="img" aria-label="Photo of a woman and a smiling man talking at a meeting table"></div>
<ul class="abs why-list">
  <li><svg width="18" height="18" viewBox="0 0 18 18"><circle cx="9" cy="9" r="7.5" fill="none" stroke="#6a2fa0" stroke-width="2"/><path d="M5 9h7M9 6l3 3-3 3" fill="none" stroke="#6a2fa0" stroke-width="2"/></svg>Transparenta kring pris</li>
  <li><svg width="18" height="18" viewBox="0 0 18 18"><circle cx="9" cy="9" r="7.5" fill="none" stroke="#6a2fa0" stroke-width="2"/><path d="M5 9h7M9 6l3 3-3 3" fill="none" stroke="#6a2fa0" stroke-width="2"/></svg>Kvalitativt nätverk och samtidigt oberoende</li>
  <li><svg width="18" height="18" viewBox="0 0 18 18"><circle cx="9" cy="9" r="7.5" fill="none" stroke="#6a2fa0" stroke-width="2"/><path d="M5 9h7M9 6l3 3-3 3" fill="none" stroke="#6a2fa0" stroke-width="2"/></svg>Feta ramavtal med otroligt nöjda kunder</li>
  <li><svg width="18" height="18" viewBox="0 0 18 18"><circle cx="9" cy="9" r="7.5" fill="none" stroke="#6a2fa0" stroke-width="2"/><path d="M5 9h7M9 6l3 3-3 3" fill="none" stroke="#6a2fa0" stroke-width="2"/></svg>Snabba och personliga</li>
  <li><svg width="18" height="18" viewBox="0 0 18 18"><circle cx="9" cy="9" r="7.5" fill="none" stroke="#6a2fa0" stroke-width="2"/><path d="M5 9h7M9 6l3 3-3 3" fill="none" stroke="#6a2fa0" stroke-width="2"/></svg>Anser återkoppling och dialog är viktigt</li>
</ul>

<footer class="abs footer"></footer>
<div class="abs foot-brand">Tarnholm</div>
<nav class="abs foot-nav">
  <a href="#">CONSULTANT</a><a href="#">CLIENT</a><a href="#">ASSIGNMENT</a><a href="#">ABOUT US</a><a href="#">CONTACT</a>
</nav>
<div class="abs rule" style="top:2940px"></div>
<div class="abs contact" style="left:197px">
  <span class="ring"><svg width="14" height="18" viewBox="0 0 14 18"><path d="M7 1a6 6 0 0 0-6 6c0 4.5 6 10 6 10s6-5.5 6-10a6 6 0 0 0-6-6z" fill="#fff"/><circle cx="7" cy="7" r="2.2" fill="#1f1f1f"/></svg></span>
  <span>Strandgatan 8<br>118 20 Stockholm</span>
</div>
<div class="abs contact" style="left:522px">
  <span class="ring"><svg width="16" height="16" viewBox="0 0 16 16"><path d="M3.5 1l2.5 3-1.5 2a9 9 0 0 0 5 5l2-1.5 3 2.5-1.5 2.5C8 15 1 8 1 2.5z" fill="#fff"/></svg></span>
  <span>+46 (0) 8-123 456 70</span>
</div>
<div class="abs contact" style="left:757px">
  <span class="ring"><svg width="18" height="14" viewBox="0 0 18 14"><rect x="1" y="1" width="16" height="12" rx="1.5" fill="#fff"/><path d="M1.5 2l7.5 6 7.5-6" fill="none" stroke="#1f1f1f" stroke-width="1.5"/></svg></span>
  <span>info@tarnholm.se</span>
</div>
<div class="abs rule" style="top:3042px"></div>
<div class="abs social"><span class="ring"></span><span class="ring"></span><span class="ring"></span></div>
<div class="abs copy">© 2022 Tarnholm. All rights reserved.</div>

</body>
</html>
```